Design graphics and Print for a line of Herb Seeds- Envelope Design

We need a set of herb seed envelopes designed for a new seed line we are launching.
The design will be both front and back

Envelope will be a colored ( green) ) envelope with white text
or a white or cream envelope in all black /and images text. Or can add some colors to the white envelope.

I have attached the die-cut of the seed envelope.
I have attached some images of envelopes I like. Please do not copy, these are just to give you an idea of what I like.

Please feel free to reach out to me if you have any questions.

Thank you

Target Market(s)

The design needs to classic that can translate to 3 different audiences. 1. young parents 2. hip, young single millennial 3. kids

Industry/Entity Type

Ecommerce

Font styles to use
Serif

Requirements
Must have
• Please use the herb - Parsley for the design
Icon, Text or both.

Front side must have:
1.either herb Icon or work Parsley or both- this will be the main attraction
2. company name- Tall Meadow Pantry
3. can use design elements
4. can use my logo on from or back or not at all. I

Backside must have:
1. social media tags
FB, Instagram and Pinterest ( use icons) @tallmeadowpantry

my website: www.tallmeadowpantry.example
this can be on from or back of the envelope.
Should not have
• please stay away from "county" flowery, old fashioned style designs

```html
<!DOCTYPE html>
<html lang="en">
<head>
<meta charset="utf-8">
<title>Tall Meadow Pantry – Seed Envelope Die Layout</title>
<link rel="stylesheet" href="https://fonts.googleapis.com/css2?family=Montserrat:wght@500;600;700&family=Tinos&display=swap">
<style>
  :root {
    --paper-gray: #d0d0d0;
    --bleed-white: #ffffff;
    --envelope-green: #3b4b3a;
    --leaf-green: #4f8f3a;
    --leaf-deep: #2f6a28;
    --lime: #97c94f;
    --cream-lime: #eefbdc;
    --die-line: #1e1e1e;
    --guide-blue: #aee0f7;
    --mark-blue: #19a7e8;
    --text-white: #ffffff;
  }
  html, body {
    margin: 0;
    padding: 0;
    overflow: hidden;
    background: var(--paper-gray);
  }
  .die-sheet {
    display: block;
    width: 1200px;
    height: 952px;
  }
  .brand-title {
    font-family: "Montserrat", sans-serif;
    font-weight: 700;
    font-size: 42px;
    fill: var(--text-white);
  }
  .brand-subtitle {
    font-family: "Montserrat", sans-serif;
    font-weight: 600;
    font-size: 26px;
    fill: var(--text-white);
  }
  .seal-name {
    font-family: "Montserrat", sans-serif;
    font-weight: 600;
    font-size: 13px;
    fill: var(--envelope-green);
  }
  .social-handle {
    font-family: "Montserrat", sans-serif;
    font-weight: 500;
    font-size: 13px;
    letter-spacing: 2px;
    fill: var(--text-white);
  }
  .website {
    font-family: "Montserrat", sans-serif;
    font-weight: 500;
    font-size: 13px;
    letter-spacing: 0.4px;
    fill: var(--text-white);
  }
  .die-spec {
    font-family: "Tinos", serif;
    font-size: 14px;
    fill: var(--die-line);
  }
  .die-spec-code {
    font-family: "Montserrat", sans-serif;
    font-size: 17px;
  }
</style>
</head>
<body>
<svg class="die-sheet" viewBox="0 0 1200 952" width="1200" height="952" xmlns="http://www.w3.org/2000/svg">
  <!-- sheet background -->
  <rect class="sheet-gray" width="1200" height="952" fill="var(--paper-gray)"/>
  <rect class="bleed-band" x="0" y="104" width="1176" height="753" fill="var(--bleed-white)"/>

  <!-- guide lines -->
  <g class="guides" stroke="var(--guide-blue)" stroke-width="2" fill="none">
    <line x1="28" y1="112" x2="28" y2="838"/>
    <path d="M53,612 V143 H336"/>
  </g>

  <!-- corner registration marks -->
  <g class="corner-marks" fill="var(--mark-blue)">
    <path d="M20,0 L40,20 H20 Z"/><path d="M0,20 L20,20 L20,40 Z"/>
    <path d="M1180,0 L1160,20 H1180 Z"/><path d="M1200,20 H1180 V40 Z"/>
    <path d="M20,952 L40,932 H20 Z"/><path d="M0,932 H20 V912 Z"/>
    <path d="M1180,952 L1160,932 H1180 Z"/><path d="M1200,932 H1180 V912 Z"/>
  </g>

  <!-- back panel -->
  <g class="back-panel">
    <path class="back-die" d="M526,113 H80 Q32,113 32,161 V789 Q32,837 80,837 H526" fill="var(--bleed-white)" stroke="var(--die-line)" stroke-width="1.5"/>
    <path class="back-fill" d="M76,166 H484 C508,166 524,148 524,113 L530,113 V837 L524,837 C524,806 508,779 484,779 H76 Z" fill="var(--envelope-green)"/>
    <rect class="back-frame" x="116" y="207" width="414" height="538" fill="none" stroke="var(--die-line)" stroke-width="1"/>

    <rect class="herb-sprig-large" role="img" aria-label="Illustrated parsley sprig" x="117" y="256" width="167" height="186" rx="60" fill="var(--leaf-green)"/>
    <rect class="herb-sprig-small" role="img" aria-label="Small parsley leaf illustration" x="428" y="604" width="96" height="84" rx="36" fill="var(--leaf-green)"/>

    <g class="social-row">
      <circle cx="278" cy="586" r="12" fill="var(--lime)"/>
      <line x1="300" y1="570" x2="300" y2="602" stroke="var(--lime)" stroke-width="1"/>
      <circle cx="323" cy="586" r="12" fill="var(--lime)"/>
      <line x1="346" y1="570" x2="346" y2="602" stroke="var(--lime)" stroke-width="1"/>
      <circle cx="369" cy="586" r="12" fill="var(--lime)"/>
    </g>
    <text class="social-handle" x="323" y="622" text-anchor="middle">@tallmeadowpantry</text>
    <text class="website" x="323" y="697" text-anchor="middle">www.tallmeadowpantry.example</text>
  </g>

  <!-- right side flap -->
  <g class="side-flap">
    <path d="M1110,113 L1164,118 Q1176,120 1176,132 V818 Q1176,830 1164,832 L1110,837 Z" fill="var(--envelope-green)" stroke="var(--die-line)" stroke-width="1.5"/>
    <path d="M1124,118 V150 Q1124,166 1140,166 H1176 V132 Q1176,120 1164,118 Z" fill="var(--bleed-white)"/>
    <path d="M1124,832 V800 Q1124,779 1140,779 H1176 V818 Q1176,830 1164,832 Z" fill="var(--bleed-white)"/>
    <rect x="1109" y="207" width="40" height="538" fill="none" stroke="var(--die-line)" stroke-width="1"/>
  </g>

  <!-- front panel with top and bottom flaps -->
  <g class="front-panel">
    <path class="front-die" d="M562,83 L574,20 Q576,14 590,14 H1060 Q1072,14 1074,26 L1078,83 L1110,113 V837 L1078,869 L1074,926 Q1072,936 1060,936 H590 Q576,936 574,926 L562,869 L530,837 V113 Z" fill="var(--envelope-green)" stroke="var(--die-line)" stroke-width="1.5"/>
    <path class="flap-top-inner" d="M588,83 V56 Q588,41 604,41 H1033 Q1049,41 1049,56 V83" fill="none" stroke="var(--die-line)" stroke-width="1"/>
    <path class="flap-bottom-inner" d="M588,869 V896 Q588,911 604,911 H1033 Q1049,911 1049,896 V869" fill="none" stroke="var(--die-line)" stroke-width="1"/>
    <line x1="562" y1="83" x2="1078" y2="83" stroke="var(--die-line)" stroke-width="1"/>
    <line x1="562" y1="869" x2="1078" y2="869" stroke="var(--die-line)" stroke-width="1"/>
    <rect class="fold-line" x="550" y="103" width="538" height="745" fill="none" stroke="var(--die-line)" stroke-width="1" stroke-dasharray="14 10"/>

    <rect class="front-window" x="570" y="122" width="496" height="705" fill="var(--envelope-green)" stroke="var(--die-line)" stroke-width="1"/>

    <path class="wave-top-band" d="M570,122 H1032 C1000,175 940,215 840,215 C760,215 720,195 660,200 L570,252 Z" fill="var(--cream-lime)"/>
    <path class="herb-pattern-top" role="img" aria-label="Scattered parsley leaf pattern on white" d="M570,122 H1020 C990,168 930,205 840,207 C770,208 720,190 660,193 L570,236 Z" fill="var(--leaf-green)"/>

    <path class="wave-bottom-band" d="M570,704 C620,630 720,585 800,590 C880,597 900,610 960,598 C1010,588 1045,555 1066,520 V827 H570 Z" fill="var(--cream-lime)"/>
    <path class="herb-pattern-bottom" role="img" aria-label="Scattered parsley leaf pattern on white" d="M570,720 C620,650 720,606 800,612 C870,618 900,640 960,632 C1010,622 1045,590 1066,562 V827 H570 Z" fill="var(--leaf-green)"/>

    <g class="brand-seal">
      <circle cx="680" cy="237" r="82" fill="var(--cream-lime)"/>
      <text class="seal-name" x="680" y="233" text-anchor="middle">Tall Meadow</text>
      <text class="seal-name" x="680" y="251" text-anchor="middle">Pantry</text>
    </g>

    <rect class="herb-leaf-right" role="img" aria-label="Small parsley leaf illustration" x="957" y="222" width="95" height="84" rx="36" fill="var(--leaf-green)"/>
    <rect class="herb-leaf-left" role="img" aria-label="Small parsley leaf illustration" x="574" y="541" width="60" height="58" rx="24" fill="var(--leaf-green)"/>

    <text class="brand-title" x="824" y="431" text-anchor="middle">TALL MEADOW</text>
    <text class="brand-subtitle" x="824" y="465" text-anchor="middle">PANTRY</text>
  </g>

  <!-- crop ticks -->
  <g class="crop-ticks" stroke="var(--guide-blue)" stroke-width="1.5">
    <line x1="520" y1="73" x2="546" y2="99"/><line x1="1112" y1="78" x2="1092" y2="100"/>
    <line x1="520" y1="879" x2="546" y2="853"/><line x1="1118" y1="882" x2="1092" y2="854"/>
  </g>

  <!-- die info -->
  <g class="die-info">
    <circle cx="93" cy="899" r="24" fill="none" stroke="var(--die-line)" stroke-width="1.2"/>
    <line x1="53" y1="899" x2="133" y2="899" stroke="var(--die-line)" stroke-width="1"/>
    <line x1="93" y1="869" x2="93" y2="929" stroke="var(--die-line)" stroke-width="1"/>
    <text class="die-spec" x="135" y="887">Die: <tspan class="die-spec-code">2BA</tspan> 3.25 x 4.5  (3 1/4 W x 4 1/2 H)</text>
    <rect class="die-note-box" x="131" y="893" width="337" height="53" fill="var(--bleed-white)"/>
  </g>
</svg>
</body>
</html>
```